Brightwell Careers Homepage Redesign

Redevelopment work is underway on the Brightwell Careers website www.brightwell-careers.com - one task is to create a more compelling vertically stacked, mobile friendly homepage. The developers are not graphic designers and have been unable to produce an effective enough design. Their latest iteration can be seen @ http://novaquill.co.uk/brightwell_careers/index_5.html

The goal of the current design job is to:

a) produce a homepage design - reworking the attached draft concepts/designs to produce an effective landing page that will entice visitors to respond to the key call to action - to book a meeting with me to discuss their needs
b) ensure the design is aesthetically/functionally aligned with the rest of the site
c) ensure the design supports responsive implementation for viewing on a full range of desktop browsers and mobile devices.

Final output should be in a .psd file with all layers unmerged.

Further details on uploaded docs.

```html
<!DOCTYPE html>
<html lang="en">
<head>
<meta charset="utf-8">
<title>Brightwell Careers – Virtual Leadership Coaching &amp; Assessment</title>
<link rel="stylesheet" href="https://fonts.googleapis.com/css2?family=Open+Sans:wght@400;600;700&display=swap">
<style>
:root{
  --orange:#f07f22;
  --orange-deep:#ee8a1c;
  --yellow:#f9c23c;
  --blue:#2b5d8f;
  --blue-light:#3c6ea6;
  --ink:#222222;
  --text:#3a3a3a;
  --muted:#8a8a8a;
  --rule:#d4d4d4;
  --band:#2a2a2a;
  --grey-section:#efefef;
  --white:#ffffff;
  --fb:#3b5998;
  --tw:#2aa9e0;
  --li:#0e76a8;
}
*{box-sizing:border-box;margin:0;padding:0}
html,body{width:1200px;height:3232px;overflow:hidden}
body{position:relative;font-family:"Open Sans",Arial,sans-serif;color:var(--text);background:var(--white)}
.abs{position:absolute}
.center{left:0;width:1200px;text-align:center}

/* header */
.site-header{top:0;left:0;width:1200px;height:149px;background:var(--white)}
.brand{left:104px;top:44px;display:flex;align-items:center;gap:12px;font-weight:700;font-size:30px;color:var(--blue)}
.brand-dot{width:46px;height:46px;border-radius:50%;background:var(--orange)}
.top-nav{right:240px;top:28px;font-size:15px;color:#666;display:flex;gap:10px}
.top-nav .active{color:var(--orange)}
.top-nav .sep{color:#ccc}
.social{display:flex;gap:11px}
.social span{width:34px;height:34px;border-radius:50%;display:block}
.social .fb{background:var(--fb)}.social .tw{background:var(--tw)}.social .li{background:var(--li)}
.header-social{right:82px;top:22px}
.main-nav{right:100px;top:89px;font-size:15px;color:#666;display:flex;gap:11px}
.main-nav .active{color:var(--blue)}
.main-nav .sep{color:#ccc}

/* hero */
.hero{top:149px;left:0;width:1200px;height:519px;background:linear-gradient(100deg,#f6c12f 0%,#f8b72c 45%,#f29a27 75%,#ef7f22 100%)}
.hero-title{left:110px;top:160px;font-size:34px;font-weight:600;line-height:43px;color:#5a3a14}
.btn-light{left:110px;top:256px;width:252px;height:50px;background:var(--white);border-radius:3px;font-size:18px;font-weight:600;color:#444;display:flex;align-items:center;justify-content:center}
.dots{left:110px;top:334px;width:102px;height:24px;border-radius:12px;background:#6b4a1c;display:flex;align-items:center;justify-content:center;gap:8px}
.dots i{width:9px;height:9px;border-radius:50%;background:var(--white);display:block}
.dots i:first-child{background:transparent;border:2px solid var(--white)}
.hero-photo{left:580px;top:0;width:520px;height:519px;background:linear-gradient(180deg,rgba(120,150,210,0) 0%,rgba(95,135,205,.55) 45%,rgba(90,130,200,.85) 100%);border-radius:220px 220px 0 0}

/* dark band */
.title-band{top:668px;left:0;width:1200px;height:133px;background:var(--band);color:var(--white);font-size:27px;font-weight:600;line-height:36px;display:flex;align-items:center;justify-content:center;text-align:center}

.vline{left:599px;width:2px;background:var(--rule)}
.outline-btn{left:431px;width:336px;border:2px solid var(--orange);border-radius:4px;color:var(--orange);font-weight:600;display:flex;align-items:center;justify-content:center}

.section-title{font-size:36px;color:var(--blue-light);font-weight:400}
.section-sub{font-size:25px;color:var(--blue);font-weight:600}
.bullet{font-size:16px;color:var(--ink);line-height:20px}
.bullet::before{content:"•";position:absolute;left:-14px}

.tagline{font-size:21px;font-weight:700;color:var(--ink);letter-spacing:1px}
.note{font-size:16px;color:var(--muted);line-height:26px}

/* audience */
.audience{top:1906px;left:0;width:1200px;height:457px;background:var(--grey-section)}
.audience h2{top:64px;font-size:29px;font-weight:700;color:var(--blue)}
.card-img{top:114px;width:288px;height:151px}
.card-title{top:298px;width:288px;text-align:center;font-size:18px;font-weight:700;color:var(--ink)}
.card-text{top:332px;width:288px;text-align:center;font-size:14.5px;line-height:22px;color:#666}

/* frame */
.frame{left:97px;top:2462px;width:1004px;height:252px;border:2px solid var(--rule);border-radius:4px}
.frame-head{top:2437px;font-size:36px;color:var(--blue-light)}
.frame-head span,.frame-foot span{background:var(--white);padding:0 18px}
.frame-line{font-size:18px;font-weight:700;color:var(--ink)}
.frame-foot{top:2687px;font-size:36px;color:var(--blue-light)}

/* cta */
.cta{top:2807px;left:0;width:1200px;height:187px;background:var(--yellow)}
.cta-text{top:38px;font-size:33px;color:#3a3a3a}
.cta-text b{font-weight:700;color:var(--ink)}
.btn-dark{left:476px;top:94px;width:248px;height:50px;background:var(--band);color:var(--white);font-size:18px;font-weight:600;display:flex;align-items:center;justify-content:center;border-radius:2px}

/* footer */
.site-footer{top:2994px;left:0;width:1200px;height:238px;background:var(--band)}
.foot-links{font-size:15px;color:var(--white)}
.foot-links .sep{color:#999;margin:0 12px}
.copyright{top:113px;font-size:14px;color:#999}
.footer-social{left:537px;top:159px}
</style>
</head>
<body>

<header class="abs site-header">
  <div class="abs brand"><span class="brand-dot"></span>Brightwell Careers</div>
  <nav class="abs top-nav"><span class="active">HOME</span><span class="sep">|</span><span>ABOUT US</span><span class="sep">|</span><span>CONTACT US</span></nav>
  <div class="abs social header-social"><span class="fb"></span><span class="tw"></span><span class="li"></span></div>
  <nav class="abs main-nav"><span class="active">Transforming Leadership</span><span class="sep">|</span><span>Assesments</span><span class="sep">|</span><span>Coaching</span><span class="sep">|</span><span>Resources &amp; Tools</span><span class="sep">|</span><span>Bookings &amp; Prices</span></nav>
</header>

<section class="abs hero">
  <h1 class="abs hero-title">WANT TO INSPIRE YOUR TEAM<br>TO REACH NEW HEIGHTS?</h1>
  <div class="abs btn-light">BOOK A MEETING NOW</div>
  <div class="abs dots"><i></i><i></i><i></i><i></i></div>
  <div class="abs hero-photo" role="img" aria-label="Photo of a coach in a blue shirt and tie gesturing while speaking"></div>
</section>

<div class="abs title-band">BRIGHTWELL CAREERS VIRTUAL LEADERSHIP<br>COACHING&amp; ASSESSMENT</div>

<div class="abs vline" style="top:823px;height:82px"></div>
<div class="abs outline-btn" style="top:926px;height:65px;font-size:34px">NEED A BOOST ?</div>
<div class="abs vline" style="top:1008px;height:80px"></div>

<h2 class="abs center section-title" style="top:1101px">You are the Leader</h2>
<p class="abs center section-sub" style="top:1146px">Your People Expect You to :</p>

<span class="abs bullet" style="left:126px;top:1207px">Engage them</span>
<span class="abs bullet" style="left:126px;top:1239px">Inspire them</span>
<span class="abs bullet" style="left:304px;top:1207px">Motivate them</span>
<span class="abs bullet" style="left:304px;top:1239px">Develop them</span>
<span class="abs bullet" style="left:513px;top:1207px">Set vision</span>
<span class="abs bullet" style="left:513px;top:1239px">Define values</span>
<span class="abs bullet" style="left:681px;top:1207px">Create culture</span>
<span class="abs bullet" style="left:681px;top:1239px">Resolve conflicts</span>
<span class="abs bullet" style="left:879px;top:1207px">Solve problems</span>
<span class="abs bullet" style="left:879px;top:1239px">Choose winning strategies</span>

<div class="abs vline" style="top:1288px;height:84px"></div>

<h2 class="abs center section-title" style="top:1386px">Partner with your Coach to :</h2>

<span class="abs bullet" style="left:120px;top:1457px">Define your goals</span>
<span class="abs bullet" style="left:120px;top:1506px">Assess your strengths</span>
<span class="abs bullet" style="left:369px;top:1457px">Define your development<br>plan</span>
<span class="abs bullet" style="left:369px;top:1506px">Explore new perspectives</span>
<span class="abs bullet" style="left:652px;top:1457px">Practice winning<br>strategies</span>
<span class="abs bullet" style="left:652px;top:1506px">Embed effective behaviours</span>
<span class="abs bullet" style="left:927px;top:1457px">Review performance<br>improvement</span>
<span class="abs bullet" style="left:927px;top:1506px">Celebrate wins!</span>

<div class="abs vline" style="top:1562px;height:86px"></div>
<div class="abs outline-btn" style="top:1665px;height:67px;font-size:34px">BOOK NOW</div>

<p class="abs center tagline" style="top:1767px">ONLINE &nbsp;•&nbsp; ANYTIME &nbsp;•&nbsp; ANYWHERE</p>
<p class="abs center note" style="top:1801px">FREE EQ-Pulse 2.0 Emotional Intelligence Leadership Assessment<br>for all Brightwell CareersCoaching Clients</p>

<section class="abs audience">
  <h2 class="abs center">WHO IS LEADERSHIP ASSESSMENT AND COACHING FOR?</h2>
  <div class="abs card-img" style="left:110px;background:linear-gradient(135deg,#f3f3f3,#d9dde2 60%,#9aa3ad)" role="img" aria-label="Photo of a business leader beside a rising chart"></div>
  <div class="abs card-img" style="left:455px;background:linear-gradient(135deg,#c9ccd0,#e8e8e8 50%,#a7b0ba)" role="img" aria-label="Photo of two managers in conversation"></div>
  <div class="abs card-img" style="left:801px;background:linear-gradient(135deg,#ececec,#f7f7f7 50%,#d7d3ce)" role="img" aria-label="Photo of a team leader at a desk"></div>

  <h3 class="abs card-title" style="left:110px">ORGANISATIONAL LEADERS</h3>
  <h3 class="abs card-title" style="left:455px">HR &amp; OD MANAGERS</h3>
  <h3 class="abs card-title" style="left:801px">TEAM LEADERS</h3>

  <p class="abs card-text" style="left:110px">" Morbi non auctor risus. Pellen tesque malesuada euismod augue ut dignissim. Suspendisse faucibus orci leo, vel ultrices purus vehicula. "</p>
  <p class="abs card-text" style="left:455px">" Morbi non auctor risus. Pellen tesque malesuada euismod augue ut dignissim. Suspendisse faucibus orci leo, vel ultrices purus vehicula. "</p>
  <p class="abs card-text" style="left:801px">" Morbi non auctor risus. Pellen tesque malesuada euismod augue ut dignissim. Suspendisse faucibus orci leo, vel ultrices purus vehicula. "</p>
</section>

<div class="abs frame"></div>
<h2 class="abs center frame-head"><span>UNLOCK YOU’RE LIMITLESS POTENTIAL</span></h2>
<p class="abs center frame-line" style="top:2539px">WORLD CLASS LEADERSHAVE MASTERED</p>
<p class="abs center frame-line" style="top:2574px">EMOTIONAL LEADERSHIPTANSORMATIONAL LEDERSHIPVALUES BASED LEADERSHIP</p>
<p class="abs center frame-line" style="top:2610px">BOOK NOW TO START YOURLEADERSHIP DEVELOPMENTJOURNEY</p>
<h2 class="abs center frame-foot"><span>BE THE BEST YOU CAN BE!</span></h2>

<section class="abs cta">
  <p class="abs center cta-text">Want to know how <b>Brightwell Careers</b> can help?</p>
  <div class="abs btn-dark">BOOK A MEETING NOW</div>
</section>

<footer class="abs site-footer">
  <p class="abs center foot-links" style="top:46px">Home<span class="sep">|</span>Transforming Leadership<span class="sep">|</span>Assesments<span class="sep">|</span>Coaching<span class="sep">|</span>Resources &amp; Tools<span class="sep">|</span>Bookings &amp; Prices</p>
  <p class="abs center foot-links" style="top:74px">About<span class="sep">|</span>Contact<span class="sep">|</span>Terms &amp; Conditions<span class="sep">|</span>Privacy Policy</p>
  <p class="abs center copyright">Copyright &nbsp;©&nbsp; 2014 &nbsp;Brightwell Careers. All rights reserved.</p>
  <div class="abs social footer-social"><span class="fb"></span><span class="tw"></span><span class="li"></span></div>
</footer>

</body>
</html>
```